Kindle Grove Wording For Logo & Business card

I have the logo, I just need the "kindle Grove" wording to go with it, and a business card design. The only thing on the business card is the website info. We provide nature connection experiences, and bolster these efforts through writing and host a platform for community around it.

I also have an idea of what it could look like (sketch), though I'm really not sure how it would come out. I am open to the best design and happy to consider original artwork. You can see what the site is about at KindleGrove.com.

Contact Information for Business Card

The only thing on the business card is the website info and the design. I will put other messaging on the back.

Website lettering (KindleGrove.com) in Montserrat

Logo Text

Kindle Grove (letters optional)

Font styles to use
Other font styles liked:
• montserrat

```html
<!DOCTYPE html>
<html lang="en">
<head>
<meta charset="utf-8">
<title>Kindle Grove – Business Card</title>
<link href="https://fonts.googleapis.com/css2?family=Montserrat:wght@400;500;600;800&display=swap" rel="stylesheet">
<style>
  :root {
    --backdrop: #c2c2c2;
    --paper: #f4f4f4;
    --paper-shade: #e9e9ea;
    --plum-deep: #211530;
    --plum: #2f1d3c;
    --plum-mid: #3d2846;
    --sunset-top: #7d5a6a;
    --sunset-glow: #e08a5a;
    --sunset-low: #6a4458;
    --ink-light: #ffffff;
  }
  * { margin: 0; padding: 0; box-sizing: border-box; }
  html, body {
    width: 1200px; height: 1000px; overflow: hidden;
    background: var(--backdrop);
    font-family: "Montserrat", sans-serif;
  }
  .card {
    position: absolute;
    left: 204px;
    width: 793px;
    height: 452px;
    overflow: hidden;
  }
  .card--front { top: 35px; background: linear-gradient(135deg, var(--paper), var(--paper-shade)); }
  .card--back { top: 513px; }

  .front-art { position: absolute; inset: 0; }

  .brand {
    position: absolute;
    left: 112px;
    top: 123px;
    width: 200px;
    text-align: center;
  }
  .brand__mark {
    width: 112px; height: 112px;
    border-radius: 50%;
    background: var(--plum-deep);
    margin: 0 auto 16px;
  }
  .brand__name {
    font-weight: 800;
    font-size: 40px;
    line-height: 42px;
    color: var(--plum);
  }

  .web-band { position: absolute; left: 0; bottom: 0; }
  .web-band__url {
    position: absolute;
    left: 41px;
    top: 414px;
    font-weight: 600;
    font-size: 19px;
    letter-spacing: 1.2px;
    color: var(--ink-light);
  }

  .back-scene {
    position: absolute; inset: 0;
    background:
      radial-gradient(ellipse at 70% 20%, rgba(90,60,80,0.45), transparent 60%),
      linear-gradient(180deg, var(--plum) 0%, var(--plum-mid) 45%, var(--plum-deep) 100%);
  }
  .back-copy {
    position: absolute;
    left: 68px;
    top: 46px;
    width: 650px;
    font-weight: 500;
    font-size: 24px;
    line-height: 47px;
    color: var(--ink-light);
  }
  .back-copy span {
    display: block;
    text-align: justify;
    text-align-last: justify;
    white-space: nowrap;
  }
</style>
</head>
<body>
  <section class="card card--front">
    <svg class="front-art" width="793" height="452" viewBox="0 0 793 452">
      <defs>
        <linearGradient id="sunset" x1="0" y1="0" x2="0" y2="1">
          <stop offset="0" stop-color="#8a6070"/>
          <stop offset="0.3" stop-color="#e08a5a"/>
          <stop offset="0.6" stop-color="#8e5a62"/>
          <stop offset="1" stop-color="#4a2f45"/>
        </linearGradient>
      </defs>
      <path role="img" aria-label="Illustrated sunset over mountains, pine forest and a lake"
            d="M228,0 H793 V175 C735,250 671,320 671,385 V452 H650 V390 C650,320 625,275 560,230 Z"
            fill="url(#sunset)"/>
      <path class="web-band" d="M0,397 H355 C366,397 372,400 377,406 L400,452 H0 Z" fill="var(--plum-deep)"/>
    </svg>

    <div class="brand">
      <div class="brand__mark"></div>
      <div class="brand__name">Kindle<br>Grove</div>
    </div>

    <p class="web-band__url">www.KindleGrove.com</p>
  </section>

  <section class="card card--back">
    <div class="back-scene" role="img" aria-label="Faint dusk landscape with hills, trees and grasses"></div>
    <p class="back-copy">
      <span>Lorem ipsum dolor sit amet, consectetuer</span>
      <span>adipiscing elit, sed diam nonummy nibh euis-</span>
      <span>mod tincidunt ut laoreet dolore magna ali-</span>
      <span>quam erat volutpat. Ut wisi enim ad minim</span>
      <span>veniam, quis nostrud exerci tation ullamcorp-</span>
      <span>er suscipit lobortis nisl ut aliquip ex ea com-</span>
      <span>modo consequat. Duis autem vel eum iriure</span>
    </p>
  </section>
</body>
</html>
```